Stationery - business cards, headers/footers, powerpoint templates
2 sets of business cards. One for 'Owen Tasker' and one for 'Lars Pemberton'. No job titles needed
Stationery - business cards, headers/footers, powerpoint templates - Consulting
Creative Brief
Simple
1. Lars Pemberton 2. Owen Tasker
Grand Cayman Cayman Islands
Lars@coverloom.ky
coverloom.ky
2 sets of business cards required - one for Lars Pemberton and one for Owen TAsker. Note that our email addresses are Lars@coverloom.ky and Owen@coverloom.ky
Modern/clean logo

```html
<!DOCTYPE html>
<html lang="en">
<head>
<meta charset="utf-8">
<title>Coverloom Solutions – Business Cards</title>
<link rel="stylesheet" href="https://fonts.googleapis.com/css2?family=Montserrat:wght@700&family=Open+Sans:wght@400;600&display=swap">
<style>
  :root {
    --page-bg: #e9e6e1;
    --card-white: #ffffff;
    --card-black: #111111;
    --brand-pink: #f47ad0;
    --ink-dark: #1a1a1a;
    --ink-light: #ffffff;
    --ink-muted: #8a8a8a;
  }
  * { margin: 0; padding: 0; box-sizing: border-box; }
  html, body {
    width: 1200px;
    height: 1039px;
    overflow: hidden;
    background: var(--page-bg);
    font-family: "Open Sans", Arial, sans-serif;
  }
  .sheet {
    width: 1200px;
    height: 1039px;
    display: flex;
    flex-direction: column;
    align-items: center;
    justify-content: center;
    gap: 40px;
  }
  .card {
    width: 770px;
    height: 440px;
    position: relative;
    overflow: hidden;
    box-shadow: 0 6px 18px rgba(0, 0, 0, 0.18);
  }

  /* Front */
  .card--front { background: var(--card-white); display: flex; flex-direction: column; }
  .front__brand-area {
    height: 250px;
    display: flex;
    flex-direction: column;
    justify-content: center;
    padding-left: 64px;
  }
  .front__tagline {
    font-size: 11px;
    letter-spacing: 1px;
    text-transform: uppercase;
    color: var(--ink-muted);
    margin-bottom: 6px;
  }
  .brand {
    display: flex;
    align-items: center;
    gap: 12px;
    font-family: "Montserrat", Arial, sans-serif;
    font-weight: 700;
    letter-spacing: -1px;
    line-height: 1;
  }
  .brand__square { background: var(--brand-pink); flex: none; }
  .brand--front { font-size: 48px; color: var(--ink-dark); }
  .brand--front .brand__square { width: 22px; height: 22px; }

  .front__name-band {
    height: 110px;
    background: var(--card-black);
    color: var(--ink-light);
    padding: 24px 64px 0;
  }
  .front__name { font-size: 26px; font-weight: 600; }
  .front__address { font-size: 14px; margin-top: 6px; color: #d8d8d8; }

  .front__contact-band {
    flex: 1;
    background: var(--brand-pink);
    color: var(--ink-dark);
    display: flex;
    align-items: center;
    padding: 0 64px;
    font-size: 15px;
    font-weight: 600;
    gap: 14px;
  }
  .contact__divider { opacity: 0.6; }

  /* Back */
  .card--back {
    background: var(--card-black);
    display: flex;
    align-items: center;
    justify-content: center;
  }
  .brand--back { font-size: 62px; color: var(--ink-light); }
  .brand--back .brand__square { width: 28px; height: 28px; }
</style>
</head>
<body>
<main class="sheet">
  <section class="card card--front" aria-label="Business card front">
    <div class="front__brand-area">
      <p class="front__tagline">insurance technology</p>
      <div class="brand brand--front">
        <span class="brand__square"></span>
        <span class="brand__name">coverloom solutions</span>
      </div>
    </div>
    <div class="front__name-band">
      <p class="front__name">Lars Pemberton</p>
      <p class="front__address">Grand Cayman, Cayman Islands</p>
    </div>
    <div class="front__contact-band">
      <span>P: +1 (345) 555-0142</span>
      <span class="contact__divider">|</span>
      <span>Lars@coverloom.ky</span>
      <span class="contact__divider">|</span>
      <span>www.coverloom.ky</span>
    </div>
  </section>

  <section class="card card--back" aria-label="Business card back">
    <div class="brand brand--back">
      <span class="brand__square"></span>
      <span class="brand__name">coverloom solutions</span>
    </div>
  </section>
</main>
</body>
</html>
```